Ridgeway Spectral Studies Website

We are a paranormal research group located in Central Mississippi. We are a group dedicated to help the community in any paranormal investigation. We use fresh new techniques with cutting edge technology to investigate any paranormal situation. Our services are always free of charge to anyone. An unique feature of our group is that we provide a complete history of the property, courtesy of our research team. We would like to see designs that incorporate our logo. We are a professional group and want a professional website.. we will need a home page that will reflect out goals. Links will include "Home, About Us, Contact us, (MAYBE MORE). We will also want a "blank page" with same links that we can edit and fill in all the information..

Target Market(s)

Paranormal-Ghost hunting groups

Industry/Entity Type

Community

Coding

Coded - Design and coding required

Number of Pages Required

2 page

Font styles to use
Other font styles liked:

Requirements
Must have
• we will need a home page that will reflect out goals. Links will include "Home, About Us, Contact us, (MAYBE MORE). We will also want a "blank page" with same links that we can edit and fill in all the information..

```html
<!DOCTYPE html>
<html lang="en">
<head>
<meta charset="utf-8">
<title>Ridgeway Spectral Studies</title>
<link rel="stylesheet" href="https://fonts.googleapis.com/css2?family=Fredoka:wght@600&family=Schoolbell&family=Hind:wght@400&display=swap">
<style>
  :root {
    --page-bg: #141414;
    --wood-dark: #2a1a0c;
    --wood-mid: #4a2f14;
    --wood-light: #6a4520;
    --header-bg: #000000;
    --ribbon: #6e4a1b;
    --ribbon-dark: #4a3010;
    --ribbon-edge: #2e1d08;
    --nav-text: #ffffff;
    --nav-active: #f2d21c;
    --panel-bg: #eef2f5;
    --ink: #111111;
    --accent-yellow: #e0c21a;
    --logo-red: #5a0c0c;
    --play-grey: rgba(150,150,150,0.75);
  }
  * { margin: 0; padding: 0; box-sizing: border-box; }
  html, body { width: 1200px; height: 1000px; overflow: hidden; background: var(--page-bg); }
  .canvas { position: relative; width: 1200px; height: 1000px; }

  .wood-frame {
    position: absolute; left: 100px; top: 40px; width: 1012px; height: 960px;
    background:
      repeating-linear-gradient(90deg, rgba(0,0,0,0.25) 0 2px, transparent 2px 9px),
      repeating-linear-gradient(0deg, transparent 0 118px, rgba(0,0,0,0.55) 118px 121px),
      linear-gradient(90deg, var(--wood-dark), var(--wood-mid) 30%, var(--wood-light) 50%, var(--wood-mid) 70%, var(--wood-dark));
  }

  .site-header {
    position: absolute; left: 123px; top: 63px; width: 965px; height: 418px;
    background: var(--header-bg);
  }
  .logo-art {
    position: absolute; left: 12px; top: 0; width: 520px; height: 418px;
    background: radial-gradient(ellipse at 50% 50%, #8a7a1a 0%, var(--logo-red) 45%, #1a0505 75%, #000 100%);
    display: flex; align-items: center; justify-content: center;
  }
  .logo-name {
    font-family: "Fredoka", sans-serif; font-weight: 600; font-size: 30px;
    color: #ffffff; letter-spacing: 1px; text-align: center;
  }

  .video-block { position: absolute; left: 509px; top: 0; width: 413px; }
  .video-title {
    font-family: "Fredoka", sans-serif; font-weight: 600; font-size: 21px;
    color: #fff; text-align: center; margin-top: 60px; letter-spacing: 0.5px;
    padding-left: 0;
  }
  .video-frame {
    position: absolute; left: 0; top: 102px; width: 413px; height: 250px;
    background: radial-gradient(ellipse at 35% 45%, #4a3c2c 0%, #1e1812 55%, #0d0a08 100%);
  }
  .play-icon { position: absolute; left: 162px; top: 75px; }

  .main-nav { position: absolute; left: 30px; top: 481px; width: 1152px; height: 60px; }
  .main-nav svg { position: absolute; left: 0; top: 0; }
  .nav-list {
    position: absolute; left: 0; top: 0; width: 100%; height: 48px;
    list-style: none; font-family: "Fredoka", sans-serif; font-weight: 600; font-size: 22px;
    color: var(--nav-text);
  }
  .nav-list li { position: absolute; top: 8px; }
  .nav-list .active { color: var(--nav-active); text-decoration: underline; text-underline-offset: 3px; }
  .nav-sep { position: absolute; top: 12px; width: 2px; height: 24px; background: #fff; }

  .content-panel {
    position: absolute; left: 123px; top: 529px; width: 965px; height: 471px;
    background: repeating-linear-gradient(90deg, rgba(0,0,0,0.015) 0 1px, transparent 1px 3px), var(--panel-bg);
  }
  .welcome-title {
    position: absolute; left: 0; top: 38px; width: 100%; text-align: center;
    font-family: "Schoolbell", cursive; font-size: 31px; color: var(--ink);
  }
  .feature-photo {
    position: absolute; left: 43px; top: 113px; width: 353px; height: 250px;
    background: radial-gradient(ellipse at 55% 50%, #6a6a6a 0%, #2e2e2e 45%, #161616 100%);
  }
  .intro-text {
    position: absolute; left: 411px; top: 112px; width: 500px;
    font-family: "Hind", sans-serif; font-size: 13px; line-height: 16.2px; color: var(--ink);
  }
  .intro-text p + p { margin-top: 16px; }
  .divider-ornament {
    position: absolute; left: 442px; top: 406px; width: 80px; height: 32px;
    background: linear-gradient(180deg, rgba(224,194,26,0.35), rgba(224,194,26,0.1));
  }
</style>
</head>
<body>
<div class="canvas">
  <div class="wood-frame"></div>

  <header class="site-header">
    <div class="logo-art" role="img" aria-label="Group emblem artwork: winged shield with banner and reaching hand">
      <span class="logo-name">Ridgeway Spectral Studies</span>
    </div>
    <section class="video-block">
      <h2 class="video-title">LATEST RESEARCH VIDEO</h2>
      <div class="video-frame" role="img" aria-label="Research video still: investigator interviewed in a dim hallway">
        <svg class="play-icon" width="106" height="106" viewBox="0 0 106 106">
          <circle cx="53" cy="53" r="47" fill="none" stroke="var(--play-grey)" stroke-width="10"/>
          <polygon points="40,30 40,76 78,53" fill="var(--play-grey)"/>
        </svg>
      </div>
    </section>
  </header>

  <nav class="main-nav">
    <svg width="1152" height="60" viewBox="0 0 1152 60">
      <polygon points="0,58 42,58 42,16 22,16 30,37" fill="var(--ribbon-dark)"/>
      <polygon points="1152,58 1110,58 1110,16 1130,16 1122,37" fill="var(--ribbon-dark)"/>
      <rect x="42" y="0" width="1068" height="48" fill="var(--ribbon)" stroke="var(--ribbon-edge)" stroke-width="2"/>
    </svg>
    <ul class="nav-list">
      <li class="active" style="left:367px">HOME</li>
      <li class="nav-sep" style="left:465px"></li>
      <li style="left:488px">ABOUT US</li>
      <li class="nav-sep" style="left:626px"></li>
      <li style="left:649px">CONTACT US</li>
    </ul>
  </nav>

  <main class="content-panel">
    <h1 class="welcome-title">Welcome on RSS - Ridgeway Spectral Studies</h1>
    <div class="feature-photo" role="img" aria-label="Black and white photo of an investigator with a camera outdoors at night"></div>
    <div class="intro-text">
      <p>Lorem ipsum dolor sit amet, consectetur adipiscing elit. Mauris cursus, mi nec viverra tristique, orci ante tristique ante, et pretium enim sem ac diam. Nunc id lacus sit amet dolor venenatis viverra. Nam ullamcorper, eros vitae auctor rutrum, tortor mi faucibus ante, posuere aliquet quam est nec turpis. Donec at malesuada nisl, et ultricies tortor. Sed vestibulum, magna in lobortis placerat, leo urna efficitur velit, et molestie ipsum eros in erat. Fusce condimentum risus ac augue vestibulum ultricies. Duis pulvinar leo et lectus sagittis malesuada. Pellentesque accumsan enim eget vulputate congue.</p>
      <p>Nam tincidunt sapien et magna aliquet, vel rhoncus lorem lobortis. Aenean tempus vel nulla sed aliquet. Vestibulum placerat ex dignissim, consequat sem nec, pretium nulla. Proin a facilisis nibh. In fringilla purus id ipsum vulputate, a mollis libero gravida.</p>
    </div>
    <div class="divider-ornament" role="img" aria-label="Small gold flourish divider"></div>
  </main>
</div>
</body>
</html>
```